Velto Bathrooms Facelift. Moving the business in to the next professional level.

I'm currently revamping my bathroom renovation business. Part of this revamp includes our marketing strategy to better position ourselves as a professional business. As the name suggests, we primarily do bathroom renovations of all shapes, sizes and budgets. I'd like a business card design that is simple, yet displays our company as sophisticated.
What I'd like is to have a card that incorporates the following elements;
- Orange set as the primary colour and Charcoal/Grey as a complement colour. The card can also include white and/or black.
- I'd like a hexagon pattern within the charcoal/grey (In gloss perhaps to break it up a bit)
- I only want the Velto Bathrooms logo on the front of the card
- Back of the card would include contact details
- The bottom edges of the card would be rounded off
- I've attached the company name. I'd like to keep velto as it is. Bathrooms can be modified
Industry/Entity Type
Marketing

```html
<!DOCTYPE html>
<html lang="en">
<head>
<meta charset="utf-8">
<title>Velto Bathrooms — Business Cards</title>
<link rel="stylesheet" href="https://fonts.googleapis.com/css2?family=Fjalla+One&family=Open+Sans:wght@400;600&display=swap">
<style>
  :root {
    --orange: #f0752f;
    --orange-deep: #d9541f;
    --orange-light: #f58a3c;
    --card-white: #f4f4f4;
    --charcoal: #4a4a4a;
    --grey: #8a8a8a;
    --backdrop: #e6e3df;
    --white: #ffffff;
  }
  * { margin: 0; padding: 0; box-sizing: border-box; }
  html, body {
    width: 1200px; height: 1023px; overflow: hidden;
    background: var(--backdrop);
    font-family: "Open Sans", Arial, sans-serif;
  }
  .canvas { position: relative; width: 1200px; height: 1023px; }

  .card {
    position: absolute;
    width: 540px; height: 310px;
    border-radius: 26px;
    box-shadow: 0 6px 18px rgba(0,0,0,0.18);
    overflow: hidden;
  }
  .card--contact { left: 70px; top: 150px; background: var(--card-white); }
  .card--brand {
    left: 590px; top: 560px;
    background: linear-gradient(135deg, var(--orange-deep) 0%, var(--orange-light) 50%, var(--orange-deep) 100%);
  }

  .wordmark {
    position: absolute;
    display: flex; align-items: center; gap: 10px;
    font-family: "Open Sans", Arial, sans-serif;
    font-weight: 600;
    font-size: 24px;
    letter-spacing: 0.5px;
    white-space: nowrap;
  }
  .wordmark__square { width: 18px; height: 18px; flex: none; }
  .card--contact .wordmark { left: 36px; top: 196px; color: var(--orange); }
  .card--contact .wordmark__square { background: var(--orange); }
  .card--brand .wordmark { left: 50%; top: 50%; transform: translate(-50%, -50%); color: var(--white); font-size: 36px; gap: 12px; }
  .card--brand .wordmark__square { border: 3px solid var(--white); width: 26px; height: 26px; }

  .contact { position: absolute; left: 320px; top: 40px; }
  .contact__name {
    font-family: "Fjalla One", "Arial Narrow", sans-serif;
    color: var(--orange); font-size: 22px; letter-spacing: 0.5px;
  }
  .contact__title { color: var(--grey); font-size: 12px; margin-top: 2px; margin-bottom: 18px; }
  .contact__line {
    display: flex; align-items: flex-start; gap: 9px;
    color: var(--charcoal); font-size: 13px; line-height: 18px; margin-bottom: 5px;
    white-space: nowrap;
  }
  .contact__line--address { margin-top: 14px; }
  .contact__icon { flex: none; width: 14px; height: 14px; margin-top: 2px; }
</style>
</head>
<body>
<main class="canvas">

  <section class="card card--contact">
    <div class="wordmark"><span class="wordmark__square"></span>Velto Bathrooms</div>

    <div class="contact">
      <p class="contact__name">Daniel R. Hale</p>
      <p class="contact__title">Director</p>

      <p class="contact__line">
        <svg class="contact__icon" viewBox="0 0 14 14" aria-hidden="true"><rect width="14" height="14" rx="2" fill="#f0752f"/><path d="M4 3.5l1.6 0 .7 2-1 .8a5 5 0 0 0 2.4 2.4l.8-1 2 .7v1.6c0 .5-.4.8-.9.8A7 7 0 0 1 3.2 4.4c0-.5.3-.9.8-.9z" fill="#fff"/></svg>
        (555) 014-2280
      </p>
      <p class="contact__line">
        <svg class="contact__icon" viewBox="0 0 14 14" aria-hidden="true"><rect width="14" height="14" rx="2" fill="#f0752f"/><rect x="3" y="6" width="8" height="5" rx="1" fill="#fff"/><rect x="4.5" y="3" width="5" height="3" fill="#fff"/></svg>
        (555) 014-2291
      </p>
      <p class="contact__line">
        <svg class="contact__icon" viewBox="0 0 14 14" aria-hidden="true"><rect width="14" height="14" rx="2" fill="#f0752f"/><rect x="3" y="4" width="8" height="6" fill="#fff"/><path d="M3 4l4 3.2L11 4" stroke="#f0752f" stroke-width="1" fill="none"/></svg>
        hello@veltobathrooms.com
      </p>
      <p class="contact__line contact__line--address">
        <svg class="contact__icon" viewBox="0 0 14 14" aria-hidden="true"><rect width="14" height="14" rx="2" fill="#f0752f"/><path d="M7 2.8a3 3 0 0 1 3 3c0 2.2-3 5.4-3 5.4S4 8 4 5.8a3 3 0 0 1 3-3z" fill="#fff"/><circle cx="7" cy="5.8" r="1.1" fill="#f0752f"/></svg>
        <span>48 Harbor Lane<br>Fairview, ST 00000</span>
      </p>
    </div>
  </section>

  <section class="card card--brand">
    <div class="wordmark"><span class="wordmark__square"></span>Velto Bathrooms</div>
  </section>

</main>
</body>
</html>
```